Harrowgate Policy Scholars' Collective Annual Symposium Poster

We need a poster to advertise for our annual symposium. The poster will be printed on 11X17" paper.

Our organization is the Harrowgate Policy Scholars' Collective. Our logo is in the uploaded files.

The title of this year's symposium is "Tidewater Chronicles - Stories Beyond Harbour." The Symposium will take place on March 31, 2017 in KW - 41.

We are accepting papers on the topics of Canada and the world; Indigenous politics in Canada; Canadian national identity; Race, racialization and belonging; Gender and politics in Canada; Queer politics and sexualities; Class and labour politics in Canada; Environmental politics; Canadian government and politics.

There will be a lunch hour roundtable discussion on the topic of "Rethreading the Loom of Civic Inquiry."
Confirmed Speakers include Dr. Corissa Pellow, Dr. Renata Quillfeather-Osorio, Dr. Tobin Merriwell, Dr. Greta Vanterpool
This round-table will consider questions of Race, Indigeneity, and Ethnicity in Political Science Research and efforts by the universities to "Decolonize," "Indigenize," and "Reconcile" the academy.
The roundtable will take place in KW-41 from 12:00 - 1:00 pm.
Lunch will be provided.

There will be a keynote panel sponsored by the Ostrander Institute for Civilian Safeguard Studies on the topic of "Borealis and the quiet art of mending."
Their logo is in the uploaded files.

For more information and a full schedule or events, visit our website: http://hpscforum.examplesite.org/acknowledgments.html

Sponsors should be listed at the bottom of the page: The Faculty of Arts, The Department of Political Science, OICSS

Target Market(s)

University students and staff who may come to the symposium

Industry/Entity Type

Political

Logo Text

HPSC Harrowgate Policy Scholars' Collective

Font styles to use
Sans Serif

Colors
ec1f27
f37122
9bcb3c
ffcf3e

Requirements
Must have
• Coulours/Leaves/etc should match this website:
• http://hpscforum.examplesite.org/acknowledgments.html
• Title of Symposium, Date, Room Number
• Sponsor logos at the bottom of the page
• Date/Time for Roundtable
Nice to have
• This list:
• We are accepting papers on the topics of Canada and the world; Indigenous politics in Canada; Canadian national identity; Race, racialization and belonging; Gender and politics in Canada; Queer politics and sexualities; Class and labour politics in Canada; Environmental politics; Canadian government and politics.
• This statement:
• This round-table will consider questions of Race, Indigeneity, and Ethnicity in Political Science Research and efforts by the universities to "Decolonize," "Indigenize," and "Reconcile" the academy.

```html
<!DOCTYPE html>
<html lang="en">
<head>
<meta charset="utf-8">
<title>Tidewater Chronicles: Stories Beyond Harbour — Symposium Poster</title>
<link rel="stylesheet" href="https://fonts.googleapis.com/css2?family=Oswald:wght@300;400&family=Ubuntu:wght@400;500&display=swap">
<style>
  :root {
    --red: #ec1f27;
    --orange: #f37122;
    --green: #9bcb3c;
    --yellow: #ffcf3e;
    --header: #3d3d3f;
    --column: #231f20;
    --paper: #efe5dd;
    --ink: #231f20;
    --footer-green: #2e8b3a;
    --footer-blue: #1b5fa8;
  }
  * { box-sizing: border-box; margin: 0; padding: 0; }
  html, body { width: 1200px; height: 1200px; overflow: hidden; background: #fff; }
  body { position: relative; font-family: "Ubuntu", sans-serif; color: var(--ink); }

  .poster { position: absolute; left: 244px; top: 42px; width: 718px; height: 1106px; background: var(--paper); overflow: hidden; }

  .header { position: absolute; left: 0; top: 0; width: 718px; height: 178px; background: var(--header); color: #fff; text-align: center; }
  .header__rule { position: absolute; left: 0; top: 5px; width: 100%; height: 5px; background: var(--red); }
  .header__org { position: absolute; top: 18px; width: 100%; font-size: 26px; }
  .header__presents { position: absolute; top: 50px; width: 100%; font-size: 20px; }
  .header__title { position: absolute; top: 78px; width: 100%; font-size: 46px; line-height: 43px; }

  .column { position: absolute; left: 0; top: 178px; width: 260px; height: 827px; background: var(--column); }
  .rule-red { position: absolute; left: 260px; height: 5px; width: 458px; background: var(--red); }
  .rule-red--top { top: 178px; }
  .rule-red--bottom { top: 993px; }
  .rule-dark { position: absolute; left: 260px; top: 998px; width: 458px; height: 7px; background: var(--column); }

  .tab { position: absolute; left: 0; width: 299px; height: 56px; background: var(--orange); color: #fff; font-family: "Oswald", sans-serif; font-weight: 400; font-size: 25px; line-height: 56px; padding-left: 16px; letter-spacing: -0.3px; }
  .tab::after { content: ""; position: absolute; left: 260px; top: 56px; border-top: 16px solid var(--red); border-right: 39px solid transparent; }

  .speakers { position: absolute; left: 16px; top: 422px; color: #fff; font-family: "Oswald", sans-serif; font-weight: 300; font-size: 14.5px; line-height: 19.6px; }
  .speakers__label { margin-bottom: 19px; }

  .info { position: absolute; left: 321px; font-weight: 500; font-size: 21px; line-height: 22px; }
  .divider { position: absolute; left: 311px; width: 375px; height: 3px; background: var(--green); }

  .roundtable { position: absolute; left: 340px; top: 414px; width: 340px; }
  .roundtable__title { font-size: 19.5px; font-weight: 500; text-decoration: underline; text-underline-offset: 3px; margin-bottom: 5px; }
  .roundtable__text { font-size: 15px; line-height: 19.5px; text-align: justify; }

  .topics { position: absolute; left: 321px; top: 578px; width: 365px; }
  .topics__heading { font-size: 21px; font-weight: 500; margin-bottom: 2px; }
  .topics__list { list-style: none; font-size: 15px; line-height: 23.5px; }
  .topics__list li { position: relative; padding-left: 19px; }
  .topics__list li::before { content: ""; position: absolute; left: 3px; top: 9px; width: 8px; height: 8px; border-radius: 50%; background: #333; }

  .keynote { position: absolute; left: 321px; top: 883px; width: 356px; }
  .keynote__title { font-size: 21px; font-weight: 500; line-height: 26px; }
  .keynote__sponsor { font-size: 15px; line-height: 20px; margin-top: 4px; padding-left: 19px; }

  .leaf { position: absolute; border-radius: 50% 50% 45% 55% / 55% 45% 55% 45%; }
  .leaf--red { left: 4px; top: 56px; width: 92px; height: 92px; background: radial-gradient(circle at 45% 45%, #f03a2e, #d8151c); }
  .leaf--yellow { left: 624px; top: 76px; width: 90px; height: 90px; background: radial-gradient(circle at 45% 45%, var(--yellow), #f3a51e); }
  .leaf--green { left: 604px; top: 228px; width: 100px; height: 96px; background: radial-gradient(circle at 45% 45%, #b5dd55, #76b833); }
  .leaf--cluster-red { left: 30px; top: 660px; width: 108px; height: 100px; background: radial-gradient(circle at 45% 45%, #b52a2a, #8c1a1f); }
  .leaf--cluster-gold { left: 148px; top: 740px; width: 90px; height: 90px; background: radial-gradient(circle at 45% 45%, #cfae3e, #a8822c); }
  .leaf--cluster-green { left: 38px; top: 782px; width: 82px; height: 78px; background: radial-gradient(circle at 45% 45%, #8bb13a, #5c8a2a); }

  .sponsors { position: absolute; left: 0; top: 1005px; width: 718px; height: 101px; display: flex; align-items: center; justify-content: space-between; padding: 0 18px; }
  .sponsor { font-size: 11.5px; font-weight: 500; line-height: 14px; display: flex; align-items: center; gap: 6px; }
  .sponsor--green { color: var(--footer-green); }
  .sponsor--blue { color: var(--footer-blue); }
  .sponsor__mark { width: 14px; height: 16px; background: var(--footer-green); flex: none; }
  .sponsor__sep { width: 1px; height: 40px; background: #333; }
</style>
</head>
<body>
<main class="poster">
  <header class="header">
    <div class="header__rule"></div>
    <p class="header__org">The Harrowgate Policy Scholars' Collective</p>
    <p class="header__presents">Presents</p>
    <h1 class="header__title">Tidewater Chronicles:<br>Stories Beyond Harbour</h1>
  </header>
  <div class="leaf leaf--red" role="img" aria-label="Red maple leaf illustration"></div>
  <div class="leaf leaf--yellow" role="img" aria-label="Yellow maple leaf illustration"></div>

  <div class="column"></div>
  <div class="rule-red rule-red--top"></div>

  <div class="tab" style="top:189px">DATE OF SYMPOSIUM</div>
  <div class="tab" style="top:269px">ROOM NUMBER</div>
  <div class="tab" style="top:349px">LUNCHTIME ROUNDTABLE</div>
  <div class="tab" style="top:578px">STUDENT PANEL DISCUSSIONS</div>
  <div class="tab" style="top:883px">KEYNOTE PANEL</div>

  <p class="info" style="top:198px">MARCH 31, 2017<br>9AM - 5PM</p>
  <div class="divider" style="top:263px"></div>
  <div class="leaf leaf--green" role="img" aria-label="Green maple leaf illustration"></div>
  <p class="info" style="top:288px">KW - 41</p>
  <div class="divider" style="top:324px"></div>

  <p class="info" style="top:356px; line-height:24px">FRIDAY, MARCH 31ST, 2017<br>12:00 - 1:00 PM</p>
  <div class="roundtable">
    <h2 class="roundtable__title">Rethreading the Loom</h2>
    <p class="roundtable__text">This round-table will consider questions of Race, Indigeneity, and Ethnicity in Political Science Research and efforts by the universities to "Decolonize," "Indigenize," and "Reconcile" the academy.</p>
  </div>

  <div class="speakers">
    <p class="speakers__label">CONFIRMED SPEAKERS:</p>
    <p>DR. CORISSA PELLOW</p>
    <p>DR. RENATA QUILLFEATHER-OSORIO</p>
    <p>DR. TOBIN MERRIWELL</p>
    <p>DR. GRETA VANTERPOOL</p>
  </div>

  <div class="divider" style="top:555px"></div>
  <div class="topics">
    <h2 class="topics__heading">Panel discussion will consider:</h2>
    <ul class="topics__list">
      <li>Canada and the World</li>
      <li>Indigenous Politics in Canada</li>
      <li>Canadian National Identity</li>
      <li>Race</li>
      <li>Racialization and Belonging</li>
      <li>Gender and Politics in Canada</li>
      <li>Queer Politics and Sexualities</li>
      <li>Class and Labour Politics in Canada</li>
      <li>Environmental politics</li>
      <li>Canadian Government and Politics.</li>
    </ul>
  </div>
  <div class="leaf leaf--cluster-red" role="img" aria-label="Dark red maple leaf illustration"></div>
  <div class="leaf leaf--cluster-gold" role="img" aria-label="Golden maple leaf illustration"></div>
  <div class="leaf leaf--cluster-green" role="img" aria-label="Green maple leaf illustration"></div>

  <div class="divider" style="top:864px"></div>
  <div class="keynote">
    <h2 class="keynote__title">Borealis and the Quiet Art of Mending</h2>
    <p class="keynote__sponsor">Sponsored by the Ostrander Institute for Civilian Safeguard Studies</p>
  </div>

  <div class="rule-red rule-red--bottom"></div>
  <div class="rule-dark"></div>

  <footer class="sponsors">
    <div class="sponsor sponsor--green"><span class="sponsor__mark"></span>Northmere University<br>Dept. of Political Science</div>
    <div class="sponsor__sep"></div>
    <div class="sponsor sponsor--blue" style="font-size:20px">HPSC</div>
    <div class="sponsor__sep"></div>
    <div class="sponsor sponsor--blue" style="font-size:20px">OICSS</div>
    <div class="sponsor__sep"></div>
    <div class="sponsor sponsor--green"><span class="sponsor__mark"></span>Northmere University<br>Faculty of Arts</div>
    <div class="sponsor__sep"></div>
    <div class="sponsor sponsor--green" style="font-size:18px">NGA</div>
  </footer>
</main>
</body>
</html>
```